Business Card Design Project For Moving Company

Hello,

We need the business card to be 2 sided and we were thinking to use the logo on the front of the card (see file 1 attached) and the text "logo" (see file 2 attached) in the back of the card. We're looking for a powerful design that will help us build our brand, as our company is new.
We are a full service moving company (no storage) located in San Diego, CA, USA. The design should communicate to our potential customers that we have the highest level of service, customer satisfaction is our number one goal, our team is professional and efficient.

Thank you,

Dorn
Updates

Project Deadline Extended
Reason: We would like to have more time to provide feedback for the designs already submitted. Thank you, Dorn

Industry/Entity Type

Moving Company

Requirements
Must have
• Front of the card must have the following text and logo:
Haulbright, Inc
Residential And Commercial
Local And Long Distance
Address: 7312 Quillmont Rd, #146,
San Diego, CA, 92784
P: 855-372-LIFT (5438)
F: 858-529-4407
info@haul-bright.com
www.haul-bright.com

Back of the card must have the following text and text "logo" (file 2 attached):

The best compliment we can ever receive is a referral from our clients.

```html
<!DOCTYPE html>
<html lang="en">
<head>
<meta charset="utf-8">
<title>Haulbright business card</title>
<link rel="stylesheet" href="https://fonts.googleapis.com/css2?family=Oswald:wght@600;700&family=Arimo:wght@400;700&display=swap">
<style>
  :root {
    --page: #ffffff;
    --card-edge: #dcdcdc;
    --arc: #e2e2e2;
    --red: #e02424;
    --muted: #555555;
    --dark-1: #3a3a3a;
    --dark-2: #1c1c1c;
    --white: #ffffff;
  }
  * { margin: 0; padding: 0; box-sizing: border-box; }
  html, body {
    width: 960px; height: 1200px; overflow: hidden;
    background: var(--page);
    font-family: "Arimo", Arial, sans-serif;
  }
  .card {
    position: absolute;
    left: 94px;
    width: 789px;
    height: 452px;
    overflow: hidden;
  }
  .card--front {
    top: 123px;
    background: var(--white);
    border: 1px solid var(--card-edge);
  }
  .front-arcs { position: absolute; inset: 0; }
  .front-name {
    position: absolute;
    left: 26px;
    top: 124px;
    font-family: "Oswald", sans-serif;
    font-weight: 700;
    font-size: 52px;
    letter-spacing: 1px;
    color: var(--red);
  }
  .referral {
    position: absolute;
    left: 27px;
    top: 360px;
    width: 420px;
    font-size: 17px;
    line-height: 24px;
    color: var(--muted);
  }
  .card--back { top: 662px; }
  .back-texture {
    position: absolute; inset: 0;
    background: radial-gradient(ellipse at 40% 35%, var(--dark-1), var(--dark-2) 80%);
  }
  .brand-tab { position: absolute; top: 0; right: 0; }
  .brand-name {
    position: absolute;
    left: 538px;
    top: 16px;
    font-family: "Oswald", sans-serif;
    font-weight: 700;
    font-size: 37px;
    line-height: 1;
    letter-spacing: 0.5px;
    color: var(--red);
  }
  .holder-name {
    position: absolute;
    left: 27px; top: 28px;
    font-weight: 700;
    font-size: 25px;
    color: var(--white);
  }
  .direct-phone {
    position: absolute;
    left: 26px; top: 206px;
    font-weight: 700;
    font-size: 62px;
    line-height: 1;
    color: var(--red);
  }
  .services {
    position: absolute;
    left: 27px; top: 289px;
    font-family: "Oswald", sans-serif;
    font-weight: 600;
    font-size: 19px;
    color: var(--white);
  }
  .contact {
    position: absolute;
    top: 383px;
    font-size: 18px;
    line-height: 23px;
    color: var(--white);
  }
  .contact--address { left: 27px; }
  .contact--phones { left: 273px; }
  .contact--web { left: 547px; }
  .divider-dot {
    position: absolute;
    top: 403px;
    width: 7px; height: 7px;
    border-radius: 50%;
    background: var(--white);
  }
  .divider-dot--one { left: 251px; }
  .divider-dot--two { left: 522px; }
</style>
</head>
<body>
  <section class="card card--front">
    <svg class="front-arcs" width="789" height="452" viewBox="0 0 789 452" aria-hidden="true">
      <circle cx="640" cy="80" r="262" fill="none" stroke="var(--arc)" stroke-width="1.5"/>
      <circle cx="680" cy="72" r="210" fill="none" stroke="var(--arc)" stroke-width="1.5"/>
    </svg>
    <div class="front-name">HAULBRIGHT</div>
    <p class="referral">The best compliment we can ever receive is a referral from our clients.</p>
  </section>

  <section class="card card--back">
    <div class="back-texture" role="img" aria-label="Dark perforated leather texture background"></div>
    <svg class="brand-tab" width="344" height="85" viewBox="0 0 344 85" aria-hidden="true">
      <polygon points="0,0 344,0 344,85 53,85" fill="var(--white)"/>
    </svg>
    <div class="brand-name">HAULBRIGHT</div>
    <div class="holder-name">Alan Wexley</div>
    <div class="direct-phone">91-9744 26 1580</div>
    <div class="services">RESIDENTIAL AND COMMERCIAL / LOCAL AND LONG DISTANCE</div>
    <div class="contact contact--address">7312 Quillmont Rd, #146,<br>San Diego, CA, 92784</div>
    <span class="divider-dot divider-dot--one"></span>
    <div class="contact contact--phones">P: 855-372-LIFT (5438)<br>F: 858-529-4407</div>
    <span class="divider-dot divider-dot--two"></span>
    <div class="contact contact--web">info@haul-bright.com<br>www.haul-bright.com</div>
  </section>
</body>
</html>
```